Client Referral Scheme

To design a brochure to advertise our client referral scheme.
Referees will be estate agents, architects, builders, tradesmen etc.
Front page: Tidewell Interiors Ltd with logo
Title: Client referral scheme
Quality German kitchens designed & installed
website address: www.tidewellinteriors.im
white background, black, grey, yellow theme as per logo
Centre pages: How the scheme works (see attachment), pictures of kitchens from brandor kitchens
Back page: info about us from our website

" attachments below are my ideas, however I want them to be far classier as per the Pemberly interiors brochure

Industry/Entity Type

Builders

Requirements
Must have
• The refer mid document attached must be the middle page

```html
<!DOCTYPE html>
<html lang="en">
<head>
<meta charset="utf-8">
<title>Client Referral Scheme – Tidewell Interiors</title>
<link rel="stylesheet" href="https://fonts.googleapis.com/css2?family=Comfortaa:wght@300;400;700&family=Dancing+Script:wght@500&family=Nunito:wght@800&display=swap">
<style>
  :root {
    --page: #ffffff;
    --sheet: #ffffff;
    --yellow: #e5c41f;
    --yellow-deep: #b8960e;
    --grey: #6f6f6f;
    --grey-light: #d9d9d9;
    --black: #1c1c1c;
    --white: #ffffff;
    --photo-dark: #6e4a2a;
    --photo-mid: #b88a5c;
    --photo-light: #efe2c8;
  }
  * { margin: 0; padding: 0; box-sizing: border-box; }
  html, body { width: 1200px; height: 891px; overflow: hidden; background: var(--page); }
  .sheet { position: absolute; left: 78px; top: 71px; width: 1044px; height: 738px; background: var(--sheet); border: 1px solid var(--grey-light); overflow: hidden; }
  .sheet-rule { position: absolute; left: 0; width: 100%; height: 6px; background: var(--yellow); }
  .sheet-rule--top { top: 0; }
  .sheet-rule--bottom { bottom: 0; }

  .title { position: absolute; left: 202px; top: 64px; width: 330px; height: 110px; font-weight: normal; }
  .title-script { position: absolute; left: 0; top: -6px; font: 500 88px/1 "Dancing Script", cursive; color: var(--yellow); }
  .title-kicker { position: absolute; left: 16px; top: 0; font: 300 16px/1 "Comfortaa", sans-serif; letter-spacing: 10px; color: var(--grey); }
  .title-tail { position: absolute; left: 112px; top: 64px; font: 400 30px/1 "Comfortaa", sans-serif; color: var(--black); }

  .hero { position: absolute; left: 0; top: 180px; width: 1044px; height: 320px;
    background: linear-gradient(100deg, var(--photo-dark) 0%, var(--photo-mid) 30%, var(--photo-light) 55%, var(--photo-mid) 75%, var(--photo-dark) 100%); }
  .hero-caption { position: absolute; right: 32px; top: 476px; font: 400 11px/1 "Comfortaa", sans-serif; color: var(--white); }

  .badge { position: absolute; left: 776px; top: 79px; width: 184px; height: 184px; }
  .badge-text { position: absolute; left: 776px; top: 79px; width: 184px; text-align: center; color: var(--white); font-family: "Comfortaa", sans-serif; }
  .badge-lead { margin-top: 40px; font-size: 13px; }
  .badge-amount { font-size: 38px; line-height: 1.1; }
  .badge-amount small { font-size: 20px; }
  .badge-note { font-size: 12.5px; line-height: 1.3; }

  .brand { position: absolute; right: 32px; top: 540px; text-align: right; font-family: "Comfortaa", sans-serif; }
  .brand-name { display: inline-flex; align-items: center; gap: 8px; font-size: 20px; font-weight: 700; color: var(--black); }
  .brand-dot { width: 14px; height: 14px; border-radius: 50%; background: var(--yellow); }
  .brand-tagline { font-size: 12px; color: var(--grey); margin-top: 5px; }

  .contact { position: absolute; left: 86px; top: 540px; color: var(--black); font-family: "Comfortaa", sans-serif; }
  .contact-phone { font-size: 17px; }
  .contact-intro { font-size: 10.5px; margin-top: 8px; color: var(--grey); }
  .contact-address { font: 800 11px/16.3px "Nunito", sans-serif; margin-top: 3px; font-style: normal; }

  .pledge { position: absolute; right: 32px; top: 636px; text-align: right; font-family: "Comfortaa", sans-serif; }
  .pledge-charity { color: var(--yellow-deep); font-size: 17px; line-height: 23px; }
  .pledge-links { color: var(--grey); font-size: 13px; line-height: 17px; margin-top: 3px; }
</style>
</head>
<body>
<main class="sheet">
  <div class="sheet-rule sheet-rule--top"></div>

  <h1 class="title">
    <span class="title-script">Referral</span>
    <span class="title-kicker">CLIENT</span>
    <span class="title-tail">scheme</span>
  </h1>

  <div class="hero" role="img" aria-label="Photograph of a fitted kitchen with wood-grain cabinets, mosaic tile splashback, gas hob and curved cream worktop"></div>
  <p class="hero-caption">the island’s premium ‘german kitchen’ studio</p>

  <svg class="badge" viewBox="0 0 184 184" aria-hidden="true">
    <circle cx="92" cy="92" r="91" fill="var(--black)"/>
    <circle cx="92" cy="92" r="89" fill="none" stroke="var(--yellow)" stroke-width="1.5"/>
    <circle cx="92" cy="92" r="78" fill="none" stroke="var(--yellow)" stroke-width="2.5"/>
  </svg>
  <div class="badge-text">
    <p class="badge-lead">Receive</p>
    <p class="badge-amount">£250<small>.00</small></p>
    <p class="badge-note">Two Hundred<br>&amp; Fifty Pound<br>referral reward</p>
  </div>

  <section class="contact">
    <p class="contact-phone">Telephone: 804127</p>
    <p class="contact-intro">Simply return the form (overleaf) to</p>
    <address class="contact-address">Tidewell Interiors Ltd,<br>Unit 4,<br>Marram Court,<br>Glenvane,<br>Portmoor,<br>Isle of Tarn,<br>TR5 2QT.</address>
  </section>

  <section class="brand">
    <p class="brand-name"><span class="brand-dot"></span>Tidewell Interiors Ltd</p>
    <p class="brand-tagline">Quality German kitchens designed &amp; installed</p>
  </section>

  <section class="pledge">
    <p class="pledge-charity">We’ll also donate £50 to Harbourlight Hospice<br>with every referral received.</p>
    <p class="pledge-links">Instant form online at: www.tidewellinteriors.im/refer<br>more info: www.tidewellinteriors.im</p>
  </section>

  <div class="sheet-rule sheet-rule--bottom"></div>
</main>
</body>
</html>
```